Package Card - Horse Products

I require a card design for the top of a package (see photo). This product is a number holder that gets pinned on to a horse bridle or saddle blanket for competitions. It is a high quality, genuine leather, and premium product.Card is 15cm across and 6cm high. Requirements:Must have - Logo, -"Equestrian Number Holder"- Place on back for barcodeAnything else is up to you! Suggestions and ideas welcome. Card back colour can be any colour.My outcome is for it to look like a premium product

Target Market(s)

High end equestrian competitors

Colors
fbf289

Requirements
Must have
• Logo
• "Equestrian Number Holder"
• "Genuine Leather"
• Room on the back for a barcode sticker
Nice to have
• Should look up market and elegant

```html
<!DOCTYPE html>
<html lang="en">
<head>
<meta charset="utf-8">
<title>Harbor Ridge Equestrian – Number Holder Package Card</title>
<link rel="stylesheet" href="https://fonts.googleapis.com/css2?family=Cinzel:wght@500;600&display=swap">
<style>
  :root {
    --backdrop: #d1d2d4;
    --card: #ffffff;
    --ink: #050608;
    --gold-deep: #c07a2c;
    --gold-mid: #e2a84a;
    --gold-light: #fbd27a;
    --brand-gold: #c99a3e;
  }
  html, body {
    margin: 0;
    padding: 0;
    width: 1200px;
    height: 999px;
    overflow: hidden;
    background: var(--backdrop);
  }
  .canvas {
    position: relative;
    width: 1200px;
    height: 999px;
    font-family: "Cinzel", "Times New Roman", serif;
    color: var(--ink);
  }
  .card-shapes {
    position: absolute;
    inset: 0;
  }
  .barcode-area {
    position: absolute;
    left: 327px;
    top: 145px;
    width: 546px;
    height: 185px;
    background: var(--ink);
    display: flex;
    align-items: center;
    justify-content: center;
  }
  .barcode-area span {
    color: #ffffff;
    font-family: "Times New Roman", serif;
    font-size: 36px;
    letter-spacing: 1px;
    transform: rotate(180deg);
  }
  .material-label {
    position: absolute;
    left: 300px;
    top: 346px;
    width: 600px;
    margin: 0;
    text-align: center;
    font-size: 51px;
    font-weight: 600;
    line-height: 50px;
    letter-spacing: 1px;
    transform: rotate(180deg);
  }
  .pin-hole {
    position: absolute;
    width: 50px;
    height: 50px;
    border-radius: 50%;
    background: var(--ink);
  }
  .pin-hole.upper { left: 575px; top: 417px; }
  .pin-hole.lower { left: 575px; top: 528px; }
  .brand-name {
    position: absolute;
    left: 100px;
    top: 648px;
    width: 1000px;
    margin: 0;
    text-align: center;
    font-size: 46px;
    font-weight: 600;
    line-height: 1;
    color: var(--brand-gold);
    letter-spacing: 2px;
    white-space: nowrap;
  }
  .product-title {
    position: absolute;
    left: 82px;
    top: 796px;
    margin: 0;
    font-size: 51px;
    font-weight: 600;
    line-height: 1;
    letter-spacing: 1px;
    white-space: nowrap;
  }
</style>
</head>
<body>
<main class="canvas">
  <svg class="card-shapes" width="1200" height="999" viewBox="0 0 1200 999" aria-hidden="true">
    <defs>
      <linearGradient id="gold-sweep" x1="0" y1="0" x2="1" y2="0">
        <stop offset="0" stop-color="#c07a2c"/>
        <stop offset="0.5" stop-color="#e2a84a"/>
        <stop offset="1" stop-color="#fbd27a"/>
      </linearGradient>
      <linearGradient id="gold-sweep-rev" x1="0" y1="0" x2="1" y2="0">
        <stop offset="0" stop-color="#fbd27a"/>
        <stop offset="0.5" stop-color="#e2a84a"/>
        <stop offset="1" stop-color="#c07a2c"/>
      </linearGradient>
    </defs>
    <rect class="card-face" x="24" y="38" width="1152" height="922" fill="#ffffff"/>
    <path class="corner-band top" d="M24,38 H800 Q420,104 24,214 Z" fill="#050608"/>
    <path class="gold-swoosh top" d="M24,214 Q420,104 800,38 L790,38 Q430,122 24,242 Z" fill="url(#gold-sweep)"/>
    <path class="gold-swoosh bottom" d="M412,960 Q800,862 1176,758 L1176,776 Q800,878 440,960 Z" fill="url(#gold-sweep-rev)"/>
    <path class="corner-band bottom" d="M440,960 Q800,878 1176,776 V960 Z" fill="#050608"/>
  </svg>

  <div class="barcode-area"><span>BARCODE</span></div>

  <p class="material-label">Genuine Leather</p>

  <div class="pin-hole upper"></div>
  <div class="pin-hole lower"></div>

  <h1 class="brand-name">HARBOR RIDGE EQUESTRIAN</h1>

  <h2 class="product-title">Equestrian Number Holder</h2>
</main>
</body>
</html>
```